Agricultural Consulting Website

Provide a modern yet business like website for my new Agriculture Consulting Business in Australia called FenTrove. Whilst we are based in Australia we are targetting both domestic and international markets (especially in Asia). We are targetting corporate, small business, government and farmer clients. The design should compliment our logo also sourced through pixel guild. The webiste should be easy for me to keep updated on a regular basis without the need to go back to the designer.

Industry/Entity Type

Business

Requirements
Must have
• clean crisp feel
• be modern yet business like
• be able to be updated by myself easily

```html
<!DOCTYPE html>
<html lang="en">
<head>
<meta charset="utf-8">
<title>FenTrove – Agricultural Consulting</title>
<link rel="stylesheet" href="https://fonts.googleapis.com/css2?family=Arimo:wght@400;700&display=swap">
<style>
  :root{
    --green-bright:#6ab816;
    --green-mid:#4f9a0c;
    --green-deep:#3a6e05;
    --brown:#6b3a0e;
    --white:#ffffff;
    --yellow:#ffd800;
    --news-date:#7dff3a;
    --btn-green:#00ee00;
    --sans:"Arimo", Arial, Helvetica, sans-serif;
  }
  *{box-sizing:border-box;margin:0;padding:0}
  html,body{width:900px;height:1200px;overflow:hidden;background:var(--white);font-family:var(--sans)}
  .page{position:relative;width:900px;height:1200px}
  .site{position:absolute;left:45px;top:0;width:806px;height:1200px}

  .masthead{position:absolute;left:0;top:0;width:806px;height:104px}
  .masthead-bg{position:absolute;left:0;top:0}
  .brand{position:absolute;left:26px;top:30px;display:flex;align-items:center;gap:10px}
  .brand-mark{width:54px;height:54px;background:var(--brown)}
  .brand-name{font-size:32px;font-weight:400;color:var(--brown);letter-spacing:0.3px}
  .contact{position:absolute;left:645px;top:32px;color:var(--white);font-size:12.5px;line-height:23px;list-style:none}
  .contact li{display:flex;align-items:center;gap:5px}
  .contact-icon{width:17px;height:17px;flex:none}

  .main-nav{position:absolute;left:0;top:104px;width:806px;height:41px;background:linear-gradient(#5aa80e,#3f8a05)}
  .main-nav ul{display:flex;list-style:none;margin-left:85px;height:41px}
  .main-nav li{height:41px;display:flex;align-items:center;padding:0 15px;color:var(--white);font-weight:700;font-size:14px;text-shadow:0 1px 1px rgba(0,0,0,.35)}
  .main-nav li+li{padding-left:15px;padding-right:15px}
  .main-nav li.current{background:var(--white);color:#111;text-shadow:none}

  .hero{position:absolute;left:0;top:148px;width:806px;height:335px;
    background:linear-gradient(180deg,#5a3a12 0%,#c98a2a 22%,#8a6a20 30%,#5a3f18 48%,#7a7a18 70%,#8f9a1c 100%)}
  .hero-dots{position:absolute;right:18px;bottom:14px;display:flex;gap:3px}
  .hero-dots span{width:11px;height:11px;border-radius:50%;background:var(--white)}
  .hero-dots span:first-child{background:transparent;border:1.5px solid var(--white)}

  .content{position:absolute;left:0;top:483px;width:533px;height:650px;background:linear-gradient(#3c7505,#2f6a04)}
  .sidebar{position:absolute;left:533px;top:483px;width:273px;height:650px;background:linear-gradient(#447e0b,#3a7406)}

  .intro{position:absolute;left:12px;top:19px;width:510px;color:var(--white)}
  .intro h1{font-size:18.5px;font-weight:700;margin-bottom:1px}
  .intro p{font-size:11.6px;line-height:20.6px;text-align:justify}
  .intro p+p{margin-top:20.6px}
  .intro p.tight{margin-top:0}

  .feature{position:absolute;left:19px;width:502px;height:140px}
  .feature-photo{position:absolute;left:0;top:0;width:198px;height:137px;border:2px solid var(--white);box-shadow:2px 3px 5px rgba(0,0,0,.4)}
  .feature-photo.tractor{background:linear-gradient(#9cc8ee 0%,#cfe2f2 28%,#3a5a2a 45%,#c49a52 70%,#a57a3a 100%)}
  .feature-photo.produce{background:radial-gradient(ellipse at 50% 55%,#6aa82c 0%,#c84a2a 40%,#f0a030 58%,#ffffff 75%)}
  .feature-text{position:absolute;left:209px;top:-4px;width:292px;color:var(--white);font-size:11.6px;line-height:19px;text-align:justify;hyphens:auto;-webkit-hyphens:auto}
  .read-more{position:absolute;left:406px;top:108px;color:var(--yellow);font-size:14px}

  .search{position:absolute;left:21px;top:27px;display:flex}
  .search-field{width:187px;height:20px;background:linear-gradient(#e6e6e6,#ffffff);border:1px solid #cfcfcf}
  .search-btn{width:48px;height:20px;margin-left:2px;background:var(--green-mid);color:var(--white);font-size:12.5px;display:flex;align-items:center;justify-content:center}

  .login{position:absolute;left:19px;top:69px;width:239px;height:196px;border:1px solid #c9dcae;background:rgba(120,160,40,.25);color:var(--white);text-align:center}
  .login h2{font-size:15px;font-weight:400;margin-top:12px}
  .login label{display:block;font-size:12px;margin-top:17px}
  .login label+.field{margin-top:7px}
  .login .field{width:200px;height:22px;margin:0 auto;background:linear-gradient(#e0e0e0,#ffffff);border:1px solid #cfcfcf}
  .login .actions{position:absolute;left:18px;right:20px;top:160px;display:flex;justify-content:space-between}
  .login .actions span{height:23px;padding:0 9px;background:var(--btn-green);color:#0a2a00;font-size:14px;display:flex;align-items:center;border:1px solid #0bb000}

  .news{position:absolute;left:21px;top:305px;width:235px;color:var(--white)}
  .news h3{font-size:14px;font-weight:400;color:var(--yellow);padding-bottom:10px;border-bottom:2px solid #d7e8c0}
  .news article{padding:7px 0 11px;border-bottom:2px solid #d7e8c0}
  .news article:last-child{border-bottom:none}
  .news time{display:block;font-size:12.5px;color:var(--news-date);margin-bottom:2px}
  .news p{font-size:9px;line-height:11.5px}

  .site-footer{position:absolute;left:0;top:1133px;width:806px;height:67px;background:linear-gradient(#5fae12,#4b9a08);color:var(--white);text-align:center}
  .site-footer ul{list-style:none;display:flex;justify-content:center;gap:22px;margin-top:18px;font-size:10.5px;font-weight:700}
  .site-footer small{display:block;font-size:11.5px;margin-top:16px}
</style>
</head>
<body>
<div class="page">
  <div class="site">
    <header class="masthead">
      <svg class="masthead-bg" width="806" height="104" viewBox="0 0 806 104" aria-hidden="true">
        <defs>
          <linearGradient id="hdr" x1="0" y1="0" x2="0" y2="1">
            <stop offset="0" stop-color="#5ba80f"/><stop offset="1" stop-color="#4a950a"/>
          </linearGradient>
        </defs>
        <rect width="806" height="104" fill="url(#hdr)"/>
        <path d="M215 0 C300 30 340 70 330 104 L210 104 Z" fill="#a3d16a" opacity=".7"/>
        <path d="M0 0 H222 C250 40 250 80 220 104 H0 Z" fill="#ffffff"/>
      </svg>
      <div class="brand">
        <span class="brand-mark"></span>
        <span class="brand-name">FenTrove</span>
      </div>
      <ul class="contact">
        <li><svg class="contact-icon" viewBox="0 0 18 18" aria-hidden="true"><circle cx="9" cy="9" r="8" fill="none" stroke="#fff" stroke-width="1.3"/><path d="M6 5 l2 0 l1 2.5 l-1.2 1 a5 5 0 0 0 2 2 l1-1.2 l2.5 1 l0 2 a7 7 0 0 1-7.3-7.3z" fill="#fff"/></svg><span>061-482907315</span></li>
        <li><svg class="contact-icon" viewBox="0 0 18 18" aria-hidden="true"><circle cx="9" cy="9" r="8" fill="none" stroke="#fff" stroke-width="1.3"/><circle cx="9" cy="9" r="2.3" fill="none" stroke="#fff" stroke-width="1.2"/><path d="M11.3 7 v3 a1.3 1.3 0 0 0 2.6 0 V9 a4.9 4.9 0 1 0 -2 4" fill="none" stroke="#fff" stroke-width="1.2"/></svg><span>hello@fentrove.example</span></li>
      </ul>
    </header>

    <nav class="main-nav">
      <ul>
        <li class="current">HOME</li><li>PRODUCT</li><li>ABOUT</li><li>FEATURES</li><li>ORDER</li><li>CONTACTS</li><li>SERVICES</li>
      </ul>
    </nav>

    <section class="hero" role="img" aria-label="Sunset over a ploughed field with a red tractor pulling a wooden trailer">
      <div class="hero-dots"><span></span><span></span><span></span></div>
    </section>

    <main class="content">
      <div class="intro">
        <h1>Welcome to our Site</h1>
        <p>Sample Text - FTA aims to promote and enhance crop consultancy as a profession.&nbsp; The organistation also facilitates the transfer of knowledge to members and acts as a means of communication between members and other industry groups.</p>
        <p>The FTA is primarily an association for those that provide agronomic advice to cotton, grains, pulse and oilseed producers in Australia. FTA's core activities focus on providing a forum for information exchange and technical training for agronomists and those with an interest in agronomy to increase the level of professionalism of members.&nbsp; Networking and the sharing of experiences and knowledge are also important.</p>
        <p class="tight">The organisation also coordinates a variety of relevant industry projects.&nbsp; The association is also able to represent the profession to the wider agricultural industry when required.</p>
      </div>

      <article class="feature" style="top:290px">
        <div class="feature-photo tractor" role="img" aria-label="Green tractor and grain cart in a harvested field"></div>
        <p class="feature-text" lang="en">Most food has always been obtained through agriculture. With increasing concern over both the methods and prod&shy;ucts of modern industrial agriculture, there has been a growing trend toward sustainable agricultural practices. This approach, partly fueled by consumer demand, encour&shy;ages biodiversity,</p>
        <span class="read-more">Read More</span>
      </article>

      <article class="feature" style="top:465px">
        <div class="feature-photo produce" role="img" aria-label="Assorted fresh vegetables and fruit"></div>
        <p class="feature-text" lang="en">Most food has always been obtained through agriculture. With increasing concern over both the methods and prod&shy;ucts of modern industrial agriculture, there has been a growing trend toward sustainable agricultural practices. This approach, partly fueled by consumer demand, encour&shy;ages biodiversity,</p>
        <span class="read-more">Read More</span>
      </article>
    </main>

    <aside class="sidebar">
      <div class="search"><span class="search-field"></span><span class="search-btn">Search</span></div>

      <div class="login">
        <h2>Member’s Login</h2>
        <label>Username</label>
        <div class="field"></div>
        <label>Password</label>
        <div class="field"></div>
        <div class="actions"><span>Login</span><span>Register</span></div>
      </div>

      <section class="news">
        <h3>News &amp; Events</h3>
        <article><time>25-10-2014</time><p>Most food has its origin in plants. Some food is obtained directly from plants; but even animals that are used as food sources are raised by feeding them food derived</p></article>
        <article><time>20-12-2013</time><p>Sample Text- Some foods not from animal or plant sources include various edible fungi, especially mush&shy;rooms. Fungi and ambient bacteria are used in the preparation of fermented and pickled foods like leavened bread,</p></article>
        <article><time>5-10-2014</time><p>Most food has its origin in plants. Some food is obtained directly from plants; but even animals that are used as food sources are raised by feeding them food derived</p></article>
        <article><time>5-08-2013</time><p>Most food has its origin in plants. Some food is obtained directly from plants; but even animals that are used as food sources are raised by feeding them food derived</p></article>
      </section>
    </aside>

    <footer class="site-footer">
      <ul><li>HOME</li><li>PRODUCT</li><li>ABOUT</li><li>FEATURES</li><li>ORDER</li><li>CONTACTS</li><li>SERVICES</li></ul>
      <small>Copyright © 2013 FenTrove</small>
    </footer>
  </div>
</div>
</body>
</html>
```